Corvale Spine & Joint Business Card

Need a business card using the logo provided. I want brand side of the card to be grey with the logo in the center of the card in white.

On the other side I leave to the designers

Target Market(s)

Personal Injury Attorneys

Industry/Entity Type

Medical

Contact Information for Business Card

Name, CEO. Cell Phone, (Hialeah, Address, Phone) (Homestead, Address, Phone) (Tallahassee, Address, Phone)

Colors

Designer to choose only greyscale colors for use in the design.

Requirements
Must have
• Logo by itself on one side

```html
<!DOCTYPE html>
<html lang="en">
<head>
<meta charset="utf-8">
<title>Corvale Spine &amp; Joint Business Card</title>
<link rel="stylesheet" href="https://fonts.googleapis.com/css2?family=Source+Sans+3:wght@400;600;700&display=swap">
<style>
  :root {
    --backdrop: #e4e4e4;
    --slate: #575a5d;
    --paper: #eeeff1;
    --mist: #8fa9b3;
    --ink: #1f2224;
    --white: #ffffff;
    --text-on-slate: #eceeef;
  }
  * { margin: 0; padding: 0; box-sizing: border-box; }
  html, body { width: 1200px; height: 1200px; overflow: hidden; }
  body {
    background: var(--backdrop);
    position: relative;
    font-family: "Source Sans 3", "Source Sans Pro", sans-serif;
  }
  .card {
    position: absolute;
    left: 264px;
    width: 682px;
    height: 390px;
    border-radius: 34px;
    overflow: hidden;
  }
  .card-front { top: 166px; background: var(--slate); }
  .card-back { top: 654px; background: var(--paper); }

  .brand {
    position: absolute;
    font-weight: 600;
    line-height: 1;
    white-space: nowrap;
  }
  .card-front .brand {
    left: 0; right: 0; top: 168px;
    text-align: center;
    font-size: 50px;
    color: var(--white);
  }
  .card-back .brand {
    right: 66px; top: 96px;
    text-align: right;
    font-size: 27px;
    color: var(--mist);
  }

  .person { position: absolute; left: 67px; top: 78px; }
  .person-name { font-size: 21px; font-weight: 700; color: var(--mist); }
  .person-role { font-size: 16px; color: var(--ink); margin-top: 2px; }
  .person-cell {
    font-size: 15px; font-weight: 700; color: var(--ink);
    margin-top: 3px; display: flex; align-items: center; gap: 8px;
  }

  .wave { position: absolute; left: 0; top: 0; width: 682px; height: 390px; }

  .offices { position: absolute; left: 0; top: 290px; width: 682px; height: 60px; }
  .office {
    position: absolute; top: 0;
    font-size: 15.5px; line-height: 20px; color: var(--text-on-slate);
  }
  .office-phone { display: flex; align-items: center; gap: 6px; }
  .office-1 { left: 67px; }
  .office-2 { left: 273px; }
  .office-3 { left: 474px; }
  .divider {
    position: absolute; top: 2px; width: 1px; height: 50px;
    background: var(--text-on-slate);
  }
  .divider-1 { left: 237px; }
  .divider-2 { left: 439px; }
</style>
</head>
<body>

  <section class="card card-front" aria-label="Card front">
    <div class="brand">Corvale Spine &amp; Joint</div>
  </section>

  <section class="card card-back" aria-label="Card back">
    <svg class="wave" viewBox="0 0 682 390" aria-hidden="true">
      <path d="M0 190 C120 205 210 238 330 232 C450 226 560 186 682 188 L682 390 L0 390 Z" fill="var(--mist)"/>
      <path d="M0 212 C120 232 200 256 300 250 C420 244 560 214 682 221 L682 390 L0 390 Z" fill="var(--white)"/>
      <path d="M0 220 C120 240 200 262 300 256 C420 250 560 222 682 229 L682 390 L0 390 Z" fill="var(--slate)"/>
    </svg>

    <div class="person">
      <div class="person-name">Renata Holloway</div>
      <div class="person-role">Chief Executive Officer</div>
      <div class="person-cell">
        <svg width="10" height="15" viewBox="0 0 10 15" aria-hidden="true">
          <rect x="0.75" y="0.75" width="8.5" height="13.5" rx="1.5" fill="none" stroke="var(--mist)" stroke-width="1.5"/>
          <line x1="4" y1="12" x2="6" y2="12" stroke="var(--mist)" stroke-width="1.2"/>
        </svg>
        +1 555-014-7720
      </div>
    </div>

    <div class="brand">Corvale Spine &amp; Joint</div>

    <div class="offices">
      <div class="office office-1">
        <div class="office-phone">
          <svg width="13" height="13" viewBox="0 0 24 24" aria-hidden="true"><path fill="var(--text-on-slate)" d="M6.6 10.8a15.1 15.1 0 0 0 6.6 6.6l2.2-2.2a1 1 0 0 1 1-.25 11.4 11.4 0 0 0 3.6.57 1 1 0 0 1 1 1V20a1 1 0 0 1-1 1A17 17 0 0 1 3 4a1 1 0 0 1 1-1h3.5a1 1 0 0 1 1 1c0 1.25.2 2.450.57 3.57a1 1 0 0 1-.25 1z"/></svg>
          555-014-0101
        </div>
        <div>214 Linden Row</div>
        <div>Tallahassee, FL 32301</div>
      </div>
      <span class="divider divider-1"></span>
      <div class="office office-2">
        <div class="office-phone">
          <svg width="13" height="13" viewBox="0 0 24 24" aria-hidden="true"><path fill="var(--text-on-slate)" d="M6.6 10.8a15.1 15.1 0 0 0 6.6 6.6l2.2-2.2a1 1 0 0 1 1-.25 11.4 11.4 0 0 0 3.6.57 1 1 0 0 1 1 1V20a1 1 0 0 1-1 1A17 17 0 0 1 3 4a1 1 0 0 1 1-1h3.5a1 1 0 0 1 1 1c0 1.25.2 2.45.57 3.57a1 1 0 0 1-.25 1z"/></svg>
          555-014-0202
        </div>
        <div>88 Harbor Lane</div>
        <div>Homestead, FL 33030</div>
      </div>
      <span class="divider divider-2"></span>
      <div class="office office-3">
        <div class="office-phone">
          <svg width="13" height="13" viewBox="0 0 24 24" aria-hidden="true"><path fill="var(--text-on-slate)" d="M6.6 10.8a15.1 15.1 0 0 0 6.6 6.6l2.2-2.2a1 1 0 0 1 1-.25 11.4 11.4 0 0 0 3.6.57 1 1 0 0 1 1 1V20a1 1 0 0 1-1 1A17 17 0 0 1 3 4a1 1 0 0 1 1-1h3.5a1 1 0 0 1 1 1c0 1.25.2 2.45.57 3.57a1 1 0 0 1-.25 1z"/></svg>
          555-014-0303
        </div>
        <div>730 Cypress Way</div>
        <div>Hialeah, Florida 33010</div>
      </div>
    </div>
  </section>

</body>
</html>
```